Dale's Business Card Design For Businesses and Customers

Create a world class business card that will engage both businesses and customers. The card should be demonstrative of a serious business person and will lead all who are given the card to make contact. It should be both friendly and powerful. The colors must match or compliment the logo. If there are any other questions, please advise and I will provide a response.

Target Market(s)

Businesses and customers

Industry/Entity Type

Restaurant

Contact Information for Business Card

Front Side:
Sir Howard "Dale" Penrose, Founder

2716 Birchmont Court
Upper Fenwick, MD 20519

301.555.0148 DC Cell
404.555.0192 ATL Cell
888.555.0173 Toll-Free Fax
dale@kettlebrookgrill.example

www.kettlebrookgrill.example

Back:
Logo
www.kettlebrookgrill.example

Font styles to use
Serif

Colors

Designer to choose colors to be used in the design.

Requirements
Must have
• Card must be classy and highlight the website and contact information.
Nice to have
• Nice, clean, and classy like the logo.

```html
<!DOCTYPE html>
<html lang="en">
<head>
<meta charset="utf-8">
<title>Dale's Business Card</title>
<link href="https://fonts.googleapis.com/css2?family=Gelasio:wght@400;500&display=swap" rel="stylesheet">
<style>
  :root {
    --bg: #e4e5e8;
    --card: #eef0f4;
    --brown: #4a1f14;
    --ink: #1e1a18;
  }
  * { margin: 0; padding: 0; box-sizing: border-box; }
  html, body { width: 1200px; height: 960px; overflow: hidden; }
  body {
    background: var(--bg);
    font-family: "Gelasio", Georgia, serif;
    color: var(--ink);
    position: relative;
  }
  .card {
    position: absolute;
    width: 700px;
    height: 400px;
    background: var(--card);
    box-shadow: 0 6px 18px rgba(0,0,0,0.12);
    overflow: hidden;
  }
  .card--back { left: 90px; top: 60px; }
  .card--front { left: 410px; top: 500px; }

  .rule { position: absolute; background: var(--brown); height: 3px; }
  .dot {
    position: absolute; width: 12px; height: 12px; border-radius: 50%;
    background: var(--brown);
  }
  .target {
    position: absolute; border-radius: 50%;
    border: 2px solid var(--brown);
    display: flex; align-items: center; justify-content: center;
  }
  .target::after {
    content: ""; width: 45%; height: 45%; border-radius: 50%; background: var(--brown);
  }

  .brand { position: absolute; text-align: center; width: 200px; }
  .brand__mark {
    width: 110px; height: 110px; border-radius: 50%;
    background: var(--brown); margin: 0 auto;
  }
  .brand__name {
    margin-top: 6px; font-size: 30px; font-weight: 400;
    color: var(--brown); letter-spacing: 1px;
  }

  .website { position: absolute; font-size: 17px; letter-spacing: 0.3px; }

  .name { position: absolute; right: 40px; top: 118px; font-size: 24px; }
  .title { position: absolute; right: 40px; top: 182px; font-size: 20px; }
  .address { position: absolute; left: 50px; top: 222px; font-size: 16px; line-height: 1.35; }
  .email { position: absolute; right: 52px; top: 262px; font-size: 15px; }

  .phone { position: absolute; text-align: center; font-size: 15px; line-height: 1.3; width: 140px; }
  .phone::before {
    content: ""; display: block; width: 12px; height: 4px;
    background: var(--brown); margin: 0 auto 16px;
  }
</style>
</head>
<body>

<section class="card card--back" aria-label="Card back">
  <div class="rule" style="left:0; top:196px; width:58px;"></div>
  <div class="target" style="left:56px; top:184px; width:28px; height:28px;"></div>
  <div class="brand" style="left:170px; top:70px;">
    <div class="brand__mark"></div>
    <div class="brand__name">Dale's</div>
  </div>
  <div class="dot" style="left:400px; top:172px;"></div>
  <div class="rule" style="left:408px; top:176px; width:292px;"></div>
  <div class="website" style="right:38px; top:146px;">www.kettlebrookgrill.example</div>
</section>

<section class="card card--front" aria-label="Card front">
  <div class="rule" style="left:0; top:120px; width:80px;"></div>
  <div class="brand" style="left:90px; top:28px;">
    <div class="brand__mark"></div>
    <div class="brand__name">Dale's</div>
  </div>
  <div class="name">Sir Howard "Dale" Penrose</div>
  <div class="rule" style="left:320px; top:162px; width:380px;"></div>
  <div class="title">Founder</div>

  <div class="target" style="left:26px; top:224px; width:14px; height:14px;"></div>
  <div class="address">2716 Birchmont Court<br>Upper Fenwick, MD 20519</div>

  <div class="email">dale@kettlebrookgrill.example</div>
  <div class="target" style="right:26px; top:264px; width:14px; height:14px;"></div>

  <div class="phone" style="left:30px; top:284px;">301.555.0148<br>DC Cell</div>
  <div class="phone" style="left:280px; top:312px;">404.555.0192<br>ATL Cell</div>
  <div class="phone" style="left:520px; top:334px;">888.555.0173<br>Toll-Free Fax</div>
</section>

</body>
</html>
```